Motorcycle Shop Business Card

New business card for Motorcycle repair and customization shop.Business name: Copper Falcon Chris Morris443-865-5190, 7214 Quarry Lane Arbutus, MD 21227. www.dale@copperfalconcustoms.example. I uploaded some motorcycle images and logo and a couple of our calendar shoots. They do not have to be used on card just examples of some of our work and past graphic work.
We work on Vantor Brennick and Custom Built Motorcycles.

Looking for front and back design

Target Market(s)

Motorcycle owners

Industry/Entity Type

Motorcycle Part

```html
<!DOCTYPE html>
<html lang="en">
<head>
<meta charset="utf-8">
<title>Copper Falcon Customs — Business Card</title>
<link href="https://fonts.googleapis.com/css2?family=Cinzel:wght@600&family=Barlow+Condensed:wght@400&display=swap" rel="stylesheet">
<style>
  :root {
    --canvas: #ececec;
    --card: #0b0b0b;
    --ink: #f2f2f2;
    --ink-soft: #d2d2d2;
    --sky-deep: #0f1c28;
    --sky-mid: #34495a;
    --sky-teal: #1f3a44;
    --cloud: #9aa5ae;
    --wing: #6b5646;
  }
  * { box-sizing: border-box; margin: 0; padding: 0; }
  html, body { width: 1200px; height: 1200px; overflow: hidden; background: var(--canvas); }
  .sheet { position: relative; width: 1200px; height: 1200px; }
  .card {
    position: absolute; left: 180px; width: 840px; height: 480px;
    background: var(--card); overflow: hidden;
    box-shadow: 0 6px 18px rgba(0,0,0,.18);
  }
  .card--back { top: 70px; display: flex; align-items: center; justify-content: center; }
  .card--front { top: 650px; }

  .brand { text-align: center; color: var(--ink); font-family: "Cinzel", serif; font-weight: 600; line-height: 1; white-space: nowrap; }
  .card--back .brand { font-size: 80px; letter-spacing: 2px; }
  .card--back .brand span { display: block; font-size: 64px; margin-top: 14px; letter-spacing: 16px; }

  .artwork {
    position: absolute; left: 0; top: 0; width: 620px; height: 480px;
    background:
      radial-gradient(ellipse 38% 22% at 36% 62%, rgba(107,86,70,.75) 0%, transparent 100%),
      radial-gradient(ellipse 45% 30% at 30% 40%, var(--cloud) 0%, rgba(154,165,174,0) 100%),
      radial-gradient(ellipse 50% 35% at 55% 78%, var(--sky-teal) 0%, transparent 100%),
      linear-gradient(180deg, var(--sky-mid) 0%, var(--sky-deep) 100%);
    -webkit-mask-image: linear-gradient(90deg, #000 0%, #000 60%, transparent 100%);
            mask-image: linear-gradient(90deg, #000 0%, #000 60%, transparent 100%);
  }
  .details { position: absolute; left: 470px; top: 44px; width: 330px; color: var(--ink); }
  .details .brand { font-size: 32px; letter-spacing: 1px; }
  .details .brand span { display: block; font-size: 28px; margin-top: 8px; letter-spacing: 8px; }
  .holder { font-family: "Cinzel", serif; font-weight: 600; font-size: 28px; letter-spacing: 2px; margin: 48px 0 44px; text-align: center; }
  .contacts { list-style: none; font-family: "Barlow Condensed", sans-serif; font-size: 18px; color: var(--ink-soft); }
  .contacts li { display: flex; align-items: center; gap: 9px; margin-bottom: 10px; white-space: nowrap; }
  .contacts svg { width: 16px; height: 16px; flex: none; fill: var(--ink-soft); }
</style>
</head>
<body>
<main class="sheet">
  <section class="card card--back">
    <div class="brand">Copper Falcon<span>CUSTOMS</span></div>
  </section>

  <section class="card card--front">
    <div class="artwork" role="img" aria-label="Illustration of a winged angel figure seated among clouds in a starry night sky"></div>
    <div class="details">
      <div class="brand">Copper Falcon<span>CUSTOMS</span></div>
      <h1 class="holder">DALE FENWICK</h1>
      <ul class="contacts">
        <li><svg viewBox="0 0 24 24"><path d="M12 2a7 7 0 0 0-7 7c0 5 7 13 7 13s7-8 7-13a7 7 0 0 0-7-7zm0 9.5A2.5 2.5 0 1 1 12 6.5a2.5 2.5 0 0 1 0 5z"/></svg>7214 Quarry Lane Arbutus, MD 21227</li>
        <li><svg viewBox="0 0 24 24"><path d="M6.6 10.8a15.1 15.1 0 0 0 6.6 6.6l2.2-2.2a1 1 0 0 1 1-.25 11.4 11.4 0 0 0 3.6.57 1 1 0 0 1 1 1V20a1 1 0 0 1-1 1A17 17 0 0 1 3 4a1 1 0 0 1 1-1h3.5a1 1 0 0 1 1 1c0 1.25.2 2.45.57 3.57a1 1 0 0 1-.25 1z"/></svg>410-555-0137</li>
        <li><svg viewBox="0 0 24 24"><path d="M12 2a10 10 0 1 0 0 20 10 10 0 0 0 0-20zm6.9 6h-2.9a15.6 15.6 0 0 0-1.4-3.6A8 8 0 0 1 18.9 8zM12 4c.8 1.2 1.5 2.5 1.9 4h-3.8c.4-1.5 1.1-2.8 1.9-4zM4.3 14a8 8 0 0 1 0-4h3.4a16 16 0 0 0 0 4zm.8 2h2.9c.3 1.3.8 2.5 1.4 3.6A8 8 0 0 1 5.1 16zM8 8H5.1a8 8 0 0 1 4.3-3.6C8.8 5.5 8.3 6.7 8 8zm4 12c-.8-1.2-1.5-2.5-1.9-4h3.8c-.4 1.5-1.1 2.8-1.9 4zm2.3-6H9.7a14.7 14.7 0 0 1 0-4h4.6a14.7 14.7 0 0 1 0 4zm.3 5.6c.6-1.1 1.1-2.3 1.4-3.6h2.9a8 8 0 0 1-4.3 3.6zm1.7-5.6a16 16 0 0 0 0-4h3.4a8 8 0 0 1 0 4z"/></svg>www.dale@copperfalconcustoms.example</li>
      </ul>
    </div>
  </section>
</main>
</body>
</html>
```